Industrial Professional Business Card Design (Vantrel Systems)

Would like professional looking business cards. Not too busy leaning towards minimal. Should have a slogan like:
"Industrial Automation and Control".

We are a tech company that programs industrial PLC computers. We also develop custom hardware solutions. Please use the logo for inspiration.

Target Market(s)

Mining, industrial, processing, automation, factory

Industry/Entity Type

Engineering

Contact Information for Business Card

Name, phone, email, website. job title.

Font styles to use
Other font styles liked:
• droid sans

Requirements
Must have
• Use colours that go well with the logo. Not too busy design.

```html
<!DOCTYPE html>
<html lang="en">
<head>
<meta charset="utf-8">
<title>Vantrel Systems – Business Card</title>
<link href="https://fonts.googleapis.com/css2?family=Noto+Sans:wght@400;700&display=swap" rel="stylesheet">
<style>
  :root {
    --stage: #282828;
    --paper: #ffffff;
    --navy: #1b4a72;
    --orange: #f26a2b;
    --ink: #1f1f1f;
    --deep-blue: #1b2a5c;
    --sea-blue: #134f78;
    --white: #ffffff;
  }
  * { margin: 0; padding: 0; box-sizing: border-box; }
  html, body {
    width: 840px; height: 1200px; overflow: hidden;
    background: var(--stage);
    font-family: "Noto Sans", "Droid Sans", Arial, sans-serif;
  }
  .stage { position: relative; width: 840px; height: 1200px; }
  .card {
    position: absolute; left: 90px; width: 660px; height: 377px;
    box-shadow: 0 3px 6px rgba(0,0,0,0.45);
    overflow: hidden;
  }
  .card-front { top: 200px; background: var(--paper); }
  .card-back {
    top: 623px;
    background: linear-gradient(30deg, var(--deep-blue) 0%, #1a3a66 45%, var(--sea-blue) 100%);
  }

  .brand-mark {
    position: absolute; border-radius: 50%;
  }
  .front-mark { left: 451px; top: 50px; width: 90px; height: 90px; background: var(--navy); }
  .brand-name {
    position: absolute; white-space: nowrap; font-weight: 400; letter-spacing: -0.5px;
  }
  .front-name { left: 374px; top: 148px; width: 246px; text-align: center; font-size: 32px; color: var(--navy); }

  .accent-bar { position: absolute; left: 0; top: 229px; width: 11px; height: 34px; background: var(--orange); }
  .person { position: absolute; left: 48px; top: 221px; }
  .person-name { font-size: 25px; font-weight: 700; letter-spacing: 0.6px; line-height: 1; color: var(--navy); }
  .person-name .surname { color: var(--orange); }
  .person-role { margin-top: 2px; font-size: 16px; color: var(--ink); letter-spacing: 0.4px; }

  .contacts { position: absolute; left: 47px; top: 280px; list-style: none; }
  .contacts li {
    display: flex; align-items: center; height: 20px; font-size: 16px;
    color: var(--ink); letter-spacing: 0.5px;
  }
  .contacts svg { width: 14px; height: 14px; margin-right: 7px; fill: var(--navy); flex: none; }

  .back-mark { left: 285px; top: 88px; width: 90px; height: 90px; background: #c9c9c9; }
  .back-name { left: 150px; top: 196px; width: 360px; text-align: center; font-size: 40px; color: var(--white); }
  .slogan {
    position: absolute; left: 0; width: 660px; top: 320px; text-align: center;
    font-size: 18.5px; font-weight: 700; color: var(--white); letter-spacing: 0.4px;
  }
</style>
</head>
<body>
<main class="stage">
  <section class="card card-front">
    <div class="brand-mark front-mark"></div>
    <div class="brand-name front-name">Vantrel Systems</div>

    <div class="accent-bar"></div>
    <div class="person">
      <div class="person-name">DANIEL <span class="surname">CORRIGAN</span></div>
      <div class="person-role">Managing Director</div>
    </div>

    <ul class="contacts">
      <li>
        <svg viewBox="0 0 16 16"><path d="M1 6c0-2 3-3 7-3s7 1 7 3v1.5h-3.5V5.5h-7v2H1z"/><path d="M3.5 8.5 5 6.5h6l1.5 2V13h-9z"/></svg>
        +X (000) 000-0000
      </li>
      <li>
        <svg viewBox="0 0 16 16"><path d="M1 4h14v1.2L8 9.5 1 5.2z"/><path d="M1 6.8 8 11l7-4.2V13H1z"/></svg>
        Info@yourdomain.com.au
      </li>
      <li>
        <svg viewBox="0 0 16 16" fill="none" stroke="#1b4a72" stroke-width="1.1"><circle cx="8" cy="8" r="6.5"/><ellipse cx="8" cy="8" rx="3" ry="6.5"/><path d="M1.5 8h13M2.5 4.8h11M2.5 11.2h11M8 1.5v13"/></svg>
        www.yourdomain.com.au
      </li>
    </ul>
  </section>

  <section class="card card-back">
    <div class="brand-mark back-mark"></div>
    <div class="brand-name back-name">Vantrel Systems</div>
    <div class="slogan">Industrial Automation and Control</div>
  </section>
</main>
</body>
</html>
```